Innovative cost reduction consultant needs to build a group of technical advisors

We need to share our message and compassion for developing cost reduction in the automotive industry. We create opportunities for immediate innovation, by developing cost reduction solutions across suppliers with related process. Attached is an existing Power Point, but it needs improvement. Most of all, a good compelling story, why experts should join us.

Target Market(s)

Automotive industry, supply chain management

Industry/Entity Type

Automotive

Font styles to use
Serif
Sans Serif

Requirements
Must have
• Better visual graphics. There are a few, but they are not as visually appearing as I would like. A graphic with data should have a better visual impact then the ones that I created. I would like to share the message, that I am providing a solution for the automotive industry. The goal is to reduce costs and improve supplier and OEM relationships. The objective is to do so by creating opportunities for immediate innovation, by developing cost reduction solutions across suppliers with related processes. This message may need a visual graphic, which is missing from the presentation.
Nice to have
• Challenge my story and presentation. Does this make sense to you, and what is your opinions of the subject. Or, a relevant news source to validate the story.
Should not have
• I have not decided on the name of the venture or logo. So, let's just use my name as the source or writer. Derek Whitcombe, Cost Reduction Specialist. Thanks,

```html
<!DOCTYPE html>
<html lang="en">
<head>
<meta charset="utf-8">
<title>Supplier Cost Reduction – Derek Whitcombe</title>
<link href="https://fonts.googleapis.com/css2?family=Raleway:wght@400;600;700&family=Merriweather:wght@400;700&display=swap" rel="stylesheet">
<style>
:root{
  --navy:#1c2f5a;
  --blue:#2f5597;
  --sky:#5b8bd6;
  --pale:#dbe5f4;
  --ink:#222;
  --muted:#666;
  --line:#c9d3e3;
  --bg:#eef0f3;
  --white:#fff;
  --green:#6fb36f;
  --amber:#f0c050;
  --red:#d9534f;
}
*{box-sizing:border-box;margin:0;padding:0}
html,body{width:1200px;height:3332px;overflow:hidden;background:var(--bg)}
body{font-family:"Raleway",Arial,sans-serif;color:var(--ink)}
.deck{display:grid;grid-template-columns:580px 580px;grid-auto-rows:316px;gap:16px;padding:12px}
.slide{position:relative;background:var(--white);overflow:hidden;box-shadow:0 1px 3px rgba(0,0,0,.15)}
.slide-title{position:absolute;left:26px;top:20px;font-size:26px;font-weight:600;color:var(--navy)}
.slide-title::after{content:"";display:block;width:100%;height:2px;background:var(--blue);margin-top:4px}
.abs{position:absolute}
.photo{position:absolute}
.small{font-size:11px;color:var(--muted);line-height:1.4}
.bullets{list-style:none;font-size:14px;line-height:1.55}
.bullets li::before{content:"\25AA";color:var(--blue);margin-right:8px}
.box{position:absolute;border:1.5px solid var(--blue);background:var(--pale);font-size:11px;display:flex;align-items:center;justify-content:center;text-align:center;padding:4px;color:var(--navy)}
.box.dark{background:var(--blue);color:var(--white);border-color:var(--navy)}
.money{font-weight:700;color:var(--navy)}
/* title slide */
.cover-caption{position:absolute;left:0;right:0;bottom:22px;text-align:center;color:var(--white);font-size:15px;line-height:1.35;padding:0 50px}
/* news */
.news-paper{position:absolute;left:14px;top:14px;width:360px;bottom:14px;font-family:"Merriweather",Georgia,serif}
.news-mast{background:var(--navy);color:var(--white);font-weight:700;font-size:22px;padding:6px 10px}
.news-head{font-size:12px;font-weight:700;margin:8px 4px 4px}
.news-body{font-size:8.5px;line-height:1.45;color:#444;margin:0 4px 5px}
.news-side{position:absolute;right:0;top:0;bottom:0;width:196px;background:var(--navy);color:var(--white);padding:26px 18px;font-size:15px;line-height:1.4}
.news-side p{margin-bottom:22px}
/* table */
.heat{position:absolute;left:26px;top:72px;border-collapse:collapse;font-size:8px}
.heat td{width:26px;height:13px;border:1px solid var(--white)}
.heat td.lbl{width:120px;background:var(--pale);color:var(--navy);padding-left:4px}
.g{background:var(--green)}.a{background:var(--amber)}.r{background:var(--red)}.p{background:#f4dcb3}
/* join */
.join{background:var(--navy)}
.join-panel{position:absolute;left:0;top:0;bottom:0;width:250px;color:var(--white);padding:30px 26px}
.join-title{font-size:36px;font-weight:700;margin-bottom:20px}
.join-box{border:1px solid var(--sky);padding:14px;font-size:12px;line-height:2}
.join-box b{display:block;font-size:14px;margin-bottom:4px}
.dot{display:inline-block;width:9px;height:9px;border-radius:50%;background:var(--sky);margin-right:8px}
</style>
</head>
<body>
<main class="deck">

  <!-- 1 cover -->
  <section class="slide">
    <div class="photo" style="inset:0;background:linear-gradient(160deg,#7d8794,#2c323b 60%,#15181d)" role="img" aria-label="Photograph of a silver car on a dark road"></div>
    <p class="cover-caption">Creating Opportunities For Immediate Innovation<br>By Developing Cost Reduction Solutions Across Suppliers With Related Processes</p>
  </section>

  <!-- 2 news -->
  <section class="slide">
    <article class="news-paper">
      <div class="news-mast">Motor Industry Review</div>
      <p class="news-head">Supplier relations with automakers drop as cost pressure rises</p>
      <p class="news-body">Annual survey results show supplier trust in the largest carmakers has fallen for a second year in a row, with price-down demands cited most often.</p>
      <p class="news-body">Suppliers say purchasing teams push for reductions without sharing the engineering support needed to reach them, straining long partnerships.</p>
      <p class="news-body">Executives interviewed believe joint projects across shared processes could recover margin faster than one-to-one negotiations ever have.</p>
      <p class="news-body">Analysts warn that unresolved tension may slow new programs, raise launch risk and push capable suppliers toward other industries.</p>
      <p class="news-body">The report recommends structured collaboration, open data on cost drivers and rewards for ideas that lower total program cost.</p>
    </article>
    <aside class="news-side">
      <p>Increasing pressure to reduce costs has created a strain on supplier relations</p>
      <p>Suppliers are not happy with any of the OEMs, or the support from the OEM</p>
    </aside>
  </section>

  <!-- 3 case study -->
  <section class="slide">
    <h2 class="slide-title">Case Study...</h2>
    <div class="photo" style="left:26px;top:78px;width:210px;height:140px;background:linear-gradient(135deg,#e6ecd9,#c9d8b8)" role="img" aria-label="Map of Ohio showing supplier locations"></div>
    <ul class="bullets abs" style="left:256px;top:86px;font-size:12px;width:300px">
      <li>20 Sheet metal suppliers in OH</li>
      <li>5 different auto supplier base</li>
      <li>Suppliers within a 200 mile radius</li>
    </ul>
    <p class="small abs" style="left:26px;top:236px;width:520px">A supplier survey was completed to identify common cost reduction needs. The data set identified gaps where the suppliers could work together on shared processes, tooling and materials.</p>
  </section>

  <!-- 4 survey gap -->
  <section class="slide">
    <h2 class="slide-title">Supplier Survey, Gap Analysis</h2>
    <table class="heat">
      <tr><td class="lbl">Raw materials</td><td class="g"></td><td class="a"></td><td class="r"></td><td class="g"></td><td class="p"></td><td class="a"></td><td class="g"></td><td class="r"></td><td class="p"></td><td class="g"></td><td class="a"></td><td class="g"></td><td class="p"></td><td class="r"></td></tr>
      <tr><td class="lbl">Material processing</td><td class="a"></td><td class="g"></td><td class="p"></td><td class="r"></td><td class="g"></td><td class="g"></td><td class="a"></td><td class="p"></td><td class="g"></td><td class="r"></td><td class="g"></td><td class="a"></td><td class="g"></td><td class="p"></td></tr>
      <tr><td class="lbl">Tooling &amp; casting</td><td class="r"></td><td class="p"></td><td class="g"></td><td class="a"></td><td class="a"></td><td class="r"></td><td class="g"></td><td class="g"></td><td class="p"></td><td class="a"></td><td class="r"></td><td class="g"></td><td class="a"></td><td class="g"></td></tr>
      <tr><td class="lbl">Machining</td><td class="g"></td><td class="g"></td><td class="a"></td><td class="p"></td><td class="r"></td><td class="g"></td><td class="p"></td><td class="a"></td><td class="g"></td><td class="g"></td><td class="p"></td><td class="r"></td><td class="g"></td><td class="a"></td></tr>
      <tr><td class="lbl">Assembly</td><td class="p"></td><td class="a"></td><td class="g"></td><td class="g"></td><td class="a"></td><td class="p"></td><td class="r"></td><td class="g"></td><td class="a"></td><td class="p"></td><td class="g"></td><td class="g"></td><td class="r"></td><td class="p"></td></tr>
      <tr><td class="lbl">Packaging</td><td class="a"></td><td class="r"></td><td class="p"></td><td class="g"></td><td class="g"></td><td class="a"></td><td class="g"></td><td class="p"></td><td class="r"></td><td class="g"></td><td class="a"></td><td class="p"></td><td class="g"></td><td class="g"></td></tr>
      <tr><td class="lbl">Transportation</td><td class="g"></td><td class="p"></td><td class="a"></td><td class="r"></td><td class="p"></td><td class="g"></td><td class="a"></td><td class="g"></td><td class="g"></td><td class="a"></td><td class="r"></td><td class="g"></td><td class="p"></td><td class="a"></td></tr>
      <tr><td class="lbl">Inspection</td><td class="r"></td><td class="g"></td><td class="g"></td><td class="a"></td><td class="p"></td><td class="r"></td><td class="g"></td><td class="a"></td><td class="p"></td><td class="g"></td><td class="g"></td><td class="a"></td><td class="r"></td><td class="g"></td></tr>
      <tr><td class="lbl">Testing</td><td class="p"></td><td class="a"></td><td class="r"></td><td class="g"></td><td class="g"></td><td class="p"></td><td class="a"></td><td class="r"></td><td class="g"></td><td class="p"></td><td class="a"></td><td class="g"></td><td class="g"></td><td class="r"></td></tr>
      <tr><td class="lbl">Logistics</td><td class="g"></td><td class="r"></td><td class="g"></td><td class="p"></td><td class="a"></td><td class="g"></td><td class="r"></td><td class="p"></td><td class="a"></td><td class="g"></td><td class="p"></td><td class="r"></td><td class="a"></td><td class="g"></td></tr>
    </table>
  </section>

  <!-- 5 survey data -->
  <section class="slide">
    <h2 class="slide-title">Supplier survey, data</h2>
    <table class="heat" style="top:80px">
      <tr><td class="lbl" style="width:80px">Steel</td><td class="r"></td><td class="a"></td><td class="g"></td><td class="g"></td></tr>
      <tr><td class="lbl" style="width:80px">Aluminum</td><td class="g"></td><td class="r"></td><td class="a"></td><td class="g"></td></tr>
      <tr><td class="lbl" style="width:80px">Tooling</td><td class="a"></td><td class="g"></td><td class="r"></td><td class="a"></td></tr>
      <tr><td class="lbl" style="width:80px">Coatings</td><td class="g"></td><td class="a"></td><td class="g"></td><td class="r"></td></tr>
    </table>
    <svg class="abs" style="left:0;top:0" width="580" height="316">
      <g stroke="#2f5597" stroke-width="1.5" fill="none">
        <path d="M292 110 H330"/><path d="M400 110 H430"/><path d="M365 128 V170"/><path d="M365 210 V236"/>
      </g>
      <g fill="#2f5597"><path d="M330 105 l8 5 -8 5z"/><path d="M430 105 l8 5 -8 5z"/><path d="M360 170 l5 8 5-8z"/></g>
    </svg>
    <div class="box" style="left:338px;top:92px;width:62px;height:36px">Survey</div>
    <div class="box" style="left:438px;top:92px;width:100px;height:36px">Common gaps</div>
    <div class="box dark" style="left:320px;top:178px;width:90px;height:32px">Shared process</div>
    <p class="small abs" style="left:26px;top:160px;width:260px">Data identified from the supplier survey shows a gap in common processes.</p>
    <div class="box" style="left:300px;top:240px;width:130px;height:36px">Immediate innovation</div>
  </section>

  <!-- 6 individual effort -->
  <section class="slide">
    <h2 class="slide-title">Individual Supplier Effort Is Not Enough</h2>
    <svg class="abs" style="left:0;top:0" width="580" height="316">
      <rect x="70" y="160" width="60" height="70" fill="#2f5597"/>
      <rect x="230" y="100" width="60" height="130" fill="#1c2f5a"/>
      <line x1="50" y1="230" x2="320" y2="230" stroke="#999"/>
      <circle cx="450" cy="160" r="70" fill="#2f5597"/>
      <path d="M450 160 L450 90 A70 70 0 0 1 512 128 Z" fill="#dbe5f4"/>
    </svg>
    <span class="abs money" style="left:64px;top:130px;font-size:22px">$6M</span>
    <span class="abs money" style="left:218px;top:70px;font-size:22px">$1.2M</span>
    <p class="small abs" style="left:26px;top:258px;width:530px">Savings from individual supplier programs alone fall short of the goal set by the OEM.</p>
  </section>

  <!-- 7 innovative -->
  <section class="slide">
    <h2 class="slide-title">Innovative Supplier Cost Reduction</h2>
    <p class="small abs" style="left:26px;top:70px;width:530px">This pilot is an opportunity to reduce costs through material and tooling consolidation across related suppliers.</p>
    <svg class="abs" style="left:0;top:0" width="580" height="316">
      <g stroke="#2f5597" stroke-width="1.5" fill="none"><path d="M160 150 L260 200"/><path d="M160 250 L260 210"/><path d="M340 205 H400"/></g>
      <path d="M400 199 l9 6 -9 6z" fill="#2f5597"/>
    </svg>
    <div class="box" style="left:60px;top:130px;width:100px;height:36px">Supplier A</div>
    <div class="box" style="left:60px;top:234px;width:100px;height:36px">Supplier B</div>
    <div class="box dark" style="left:260px;top:186px;width:80px;height:40px">Shared solution</div>
    <div class="box" style="left:412px;top:186px;width:110px;height:40px">Innovation hub</div>
  </section>

  <!-- 8 collaborative -->
  <section class="slide">
    <h2 class="slide-title">Collaborative effort</h2>
    <ul class="bullets abs" style="left:26px;top:72px;width:530px;font-size:12px">
      <li>Leveraging the power of a full supplier base</li>
      <li>Identifying a healthy effort towards significant reduction targets</li>
      <li>Using the combined buying power of $1.6M cost of raw materials</li>
    </ul>
    <div class="box" style="left:60px;top:158px;width:200px;height:32px">Production Forecast</div>
    <div class="box" style="left:320px;top:158px;width:200px;height:32px">ROI Development</div>
    <div class="box dark" style="left:190px;top:200px;width:200px;height:32px">Shared</div>
    <div class="box" style="left:60px;top:244px;width:200px;height:32px">Supplier Group (pilot)</div>
    <div class="box" style="left:320px;top:244px;width:200px;height:32px">Next Best Solution</div>
  </section>

  <!-- 9 strength -->
  <section class="slide">
    <h2 class="slide-title">Strength</h2>
    <svg class="abs" style="left:0;top:0" width="580" height="316">
      <rect x="100" y="170" width="90" height="60" fill="#2f5597"/>
      <rect x="220" y="90" width="130" height="140" fill="#1c2f5a"/>
      <path d="M190 160 L220 110" stroke="#2f5597" stroke-width="2"/>
    </svg>
    <span class="abs" style="left:110px;top:182px;color:#fff;font-size:22px;font-weight:700">$6M</span>
    <span class="abs" style="left:238px;top:138px;color:#fff;font-size:34px;font-weight:700">$6M</span>
    <span class="abs small" style="left:106px;top:152px">Individual</span>
    <span class="abs small" style="left:266px;top:72px">Target</span>
    <p class="small abs" style="left:26px;top:248px;width:530px">The strength of a supplier group turns a small individual saving into the full target value through a shared strategy.</p>
  </section>

  <!-- 10 collaborative curve -->
  <section class="slide">
    <h2 class="slide-title">Supplier collaborative effort</h2>
    <svg class="abs" style="left:0;top:0" width="580" height="316">
      <line x1="70" y1="270" x2="520" y2="270" stroke="#999"/>
      <line x1="70" y1="270" x2="70" y2="80" stroke="#999"/>
      <path d="M80 260 C 220 250, 330 200, 480 100" stroke="#2f5597" stroke-width="3" fill="none"/>
      <g fill="#1c2f5a"><circle cx="160" cy="250" r="5"/><circle cx="280" cy="222" r="5"/><circle cx="390" cy="168" r="5"/><circle cx="480" cy="100" r="5"/></g>
    </svg>
    <span class="abs small" style="left:420px;top:72px">Group savings</span>
    <span class="abs small" style="left:130px;top:226px">Single supplier</span>
  </section>

  <!-- 11 going beyond -->
  <section class="slide">
    <h2 class="slide-title" style="font-size:17px;width:530px;text-align:center;left:25px">Going Beyond From The Most Advanced Supplier Cooperation And Innovative Models And Inviting Strategic Innovation Opportunities</h2>
    <svg class="abs" style="left:0;top:0" width="580" height="316">
      <circle cx="90" cy="170" r="30" fill="none" stroke="#2f5597" stroke-width="3"/>
      <path d="M80 200 h20 v12 h-20z" fill="#2f5597"/>
      <g stroke="#2f5597" stroke-width="1.5"><path d="M130 170 H200"/><path d="M380 170 H440"/></g>
      <path d="M200 164 l9 6 -9 6z M440 164 l9 6 -9 6z" fill="#2f5597"/>
    </svg>
    <div class="box dark" style="left:212px;top:144px;width:166px;height:52px">Supplier Cost Reduction</div>
    <div class="photo" style="left:454px;top:148px;width:100px;height:44px;background:linear-gradient(180deg,#b8c2cf,#6b7684);border-radius:6px" role="img" aria-label="Car"></div>
    <p class="small abs" style="left:26px;top:262px;width:530px;text-align:center">Integrating technology connects the OEM with a full spectrum of innovation.</p>
  </section>

  <!-- 12 greater level -->
  <section class="slide">
    <h2 class="slide-title" style="font-size:20px;width:530px">Collaborating at an even greater level to achieve momentous cost reduction goals.</h2>
    <svg class="abs" style="left:0;top:0" width="580" height="316">
      <g fill="#2f5597" opacity=".9"><circle cx="110" cy="190" r="42"/><circle cx="190" cy="140" r="34"/><circle cx="190" cy="245" r="34"/><circle cx="280" cy="190" r="42"/></g>
      <path d="M340 190 H410" stroke="#1c2f5a" stroke-width="2"/><path d="M410 184 l9 6 -9 6z" fill="#1c2f5a"/>
    </svg>
    <span class="abs" style="left:82px;top:182px;color:#fff;font-size:12px">Suppliers</span>
    <span class="abs" style="left:166px;top:133px;color:#fff;font-size:11px">Material</span>
    <span class="abs" style="left:168px;top:238px;color:#fff;font-size:11px">Tooling</span>
    <span class="abs" style="left:258px;top:182px;color:#fff;font-size:12px">Process</span>
    <div class="box" style="left:424px;top:164px;width:120px;height:52px">Supplier Cost Reduction</div>
  </section>

  <!-- 13 best practices -->
  <section class="slide">
    <h2 class="slide-title">Best practices, collaborative effort</h2>
    <ul class="bullets abs" style="left:26px;top:72px;width:530px;font-size:13px;line-height:1.5">
      <li>Incorporating best practices and shared success, supplier groups can achieve momentous cost reduction</li>
      <li>Raw Materials</li>
      <li>Material processing</li>
      <li>Tooling &amp; Casting</li>
      <li>Machining</li>
      <li>Assembly</li>
      <li>Packaging / Transportation</li>
      <li>Inspection &amp; Testing</li>
    </ul>
  </section>

  <!-- 14 project example -->
  <section class="slide">
    <h2 class="slide-title">Project example, new material</h2>
    <div class="photo" style="left:26px;top:80px;width:150px;height:110px;background:linear-gradient(135deg,#d5dbe3,#8f9aa8)" role="img" aria-label="Photograph of a stamped metal part"></div>
    <div class="photo" style="left:200px;top:80px;width:170px;height:110px;background:linear-gradient(90deg,#3a5bc7,#47c26a,#f0d040,#e0502a)" role="img" aria-label="Forming simulation heat map of the part"></div>
    <div class="photo" style="left:390px;top:80px;width:164px;height:110px;background:linear-gradient(90deg,#3a5bc7,#f0d040,#e0502a)" role="img" aria-label="Thickness analysis heat map"></div>
    <p class="small abs" style="left:26px;top:206px;width:530px">Change to high strength material reduced part weight and gauge. $1.2M per year potential savings.</p>
  </section>

  <!-- 15 one example -->
  <section class="slide">
    <h2 class="slide-title">One example, and many others</h2>
    <p class="abs" style="left:26px;top:84px;font-size:15px;color:var(--muted)">Leveraging best practices</p>
  </section>

  <!-- 16 planning venn -->
  <section class="slide">
    <h2 class="slide-title" style="font-size:22px">Project planning, forecast data, ROI, GAP analysis</h2>
    <ul class="bullets abs" style="left:26px;top:76px;width:250px;font-size:10.5px;line-height:1.5">
      <li>Plan is based on forecast data from OEM programs across suppliers</li>
      <li>ROI built from shared savings</li>
      <li>Gap analysis with all members</li>
      <li>Timeline and targets set by the group</li>
    </ul>
    <svg class="abs" style="left:0;top:0" width="580" height="316">
      <g opacity=".8"><circle cx="380" cy="150" r="62" fill="#2f5597"/><circle cx="460" cy="150" r="62" fill="#5b8bd6"/><circle cx="420" cy="220" r="62" fill="#1c2f5a"/></g>
    </svg>
    <span class="abs" style="left:344px;top:140px;color:#fff;font-size:12px">Forecast</span>
    <span class="abs" style="left:470px;top:140px;color:#fff;font-size:12px">ROI</span>
    <span class="abs" style="left:392px;top:240px;color:#fff;font-size:12px">GAP</span>
  </section>

  <!-- 17 data analytics -->
  <section class="slide">
    <h2 class="slide-title">Data analytics</h2>
    <svg class="abs" style="left:0;top:0" width="580" height="316">
      <line x1="40" y1="230" x2="330" y2="230" stroke="#999"/>
      <path d="M40 210 L100 190 L160 200 L220 150 L280 130 L330 90" stroke="#2f5597" stroke-width="3" fill="none"/>
      <path d="M40 220 L100 215 L160 205 L220 195 L280 180 L330 170" stroke="#5b8bd6" stroke-width="2" fill="none"/>
    </svg>
    <div class="photo" style="left:350px;top:150px;width:204px;height:120px;background:linear-gradient(160deg,#c7cfd9,#58626f)" role="img" aria-label="Photograph of a group of cars"></div>
  </section>

  <!-- 18 next step -->
  <section class="slide">
    <h2 class="slide-title">Next step</h2>
    <ul class="bullets abs" style="left:60px;top:100px;width:480px;font-size:15px;line-height:1.7">
      <li>Build action group</li>
      <li>Process for Norland Motors</li>
      <li>Derek's relationship with Norland NSP</li>
      <li>Meeting with Norland R&amp;D purchasing</li>
    </ul>
  </section>

  <!-- 19 join -->
  <section class="slide join">
    <div class="join-panel">
      <h2 class="join-title">Join Us!</h2>
      <div class="join-box">
        <b>Contact Information</b>
        <div><span class="dot"></span>Derek Whitcombe</div>
        <div><span class="dot"></span>(555) 014-2286</div>
        <div><span class="dot"></span>Columbus, OH</div>
        <div><span class="dot"></span>derek@costgroup.example</div>
      </div>
    </div>
    <div class="photo" style="left:250px;top:0;right:0;bottom:0;background:linear-gradient(160deg,#9aa3ad,#3a414b 60%,#1c2025)" role="img" aria-label="Photograph of a car under studio lighting"></div>
  </section>

</main>
</body>
</html>
```